BrewHaunt coffee packaging design

We need a vector design (AI) for the printing of our coffee bags.

The bags are double sided. Front will be simple with logo and web address. Back will have lots of information (below) and the wording can be changed to suit if required.

Actual bag dimensions are: 240mm wide x 335mm high (each side) artwork should be inside those sizes.

Front:
Requires - BrewHaunt cup logo, web address (brewhaunt.com.au) in lowercase Papyrus font and the words BREW HAUNT in uppercase.
**added** The front will also need a 90mm x 35mm no artwork area so we can place a sticker.

Back:
1.
Velvet Kettle Logo (needs to be entire unmodified logo) and the tagline of "Overall winner of Australia's biggest coffee roasting competition"

2.
BrewHaunt is a family business, proudly Australian owned and operated. We strive to provide amazing coffee, excellent service and great value to all our customers.

3.
Our coffee is fresh roasted to order and shipped same day.

4.
50c from every kilogram sold goes directly to projects in coffee growing regions. TrueLoop is the Fairest Trade of all - see: trueloop.net

Logos are attached and higher resolution ones are available if needed.

Requirements
Must have
• Per the description, BrewHaunt logo and webaddress on the front and Velvet Kettle logo on the back are required.

```html
<!DOCTYPE html>
<html lang="en">
<head>
<meta charset="utf-8">
<title>BrewHaunt – Green Coffee Bag Front</title>
<link rel="stylesheet" href="https://fonts.googleapis.com/css2?family=Cinzel:wght@500&family=Josefin+Sans:wght@400&family=Philosopher&display=swap">
<style>
  :root {
    --backdrop: #f2f2f2;
    --bag-black: #141414;
    --ink-white: #f4f4f4;
    --ink-soft: #d8d8d8;
    --rule-grey: #bdbdbd;
    --brand-green: #3f9a2c;
    --ribbon-green: #45a530;
    --ribbon-shade: #2f7a1f;
  }
  * { margin: 0; padding: 0; box-sizing: border-box; }
  html, body {
    width: 1200px;
    height: 900px;
    overflow: hidden;
    background: var(--backdrop);
  }
  .canvas {
    position: relative;
    width: 1200px;
    height: 900px;
  }
  .bag-front {
    position: absolute;
    left: 420px;
    top: 122px;
    width: 400px;
    height: 620px;
    background: var(--bag-black);
    color: var(--ink-white);
    text-align: center;
  }
  .category {
    position: absolute;
    top: 151px;
    left: 0;
    right: 0;
    display: flex;
    justify-content: center;
    align-items: center;
    gap: 10px;
    font-family: "Josefin Sans", sans-serif;
    font-size: 15px;
    letter-spacing: 0.5px;
    color: var(--ink-soft);
  }
  .category::before,
  .category::after,
  .net-weight::before,
  .net-weight::after {
    content: "";
    width: 20px;
    height: 1px;
    background: var(--rule-grey);
  }
  .brand-name {
    position: absolute;
    top: 186px;
    left: 0;
    right: 0;
    font-family: "Cinzel", serif;
    font-weight: 500;
    font-size: 50px;
    line-height: 48px;
    letter-spacing: 1px;
    color: var(--ink-white);
  }
  .brand-mark {
    position: absolute;
    top: 366px;
    left: 0;
    right: 0;
    display: flex;
    justify-content: center;
    align-items: center;
    gap: 10px;
    font-family: "Cinzel", serif;
    font-weight: 500;
    font-size: 26px;
    color: var(--brand-green);
  }
  .brand-mark .dot {
    width: 18px;
    height: 18px;
    border-radius: 50%;
    background: var(--brand-green);
  }
  .web-ribbon {
    position: absolute;
    top: 490px;
    left: 50%;
    transform: translateX(-50%);
    width: 200px;
    height: 36px;
  }
  .web-ribbon svg { position: absolute; inset: 0; }
  .web-address {
    position: absolute;
    inset: 0;
    display: flex;
    align-items: center;
    justify-content: center;
    font-family: "Philosopher", sans-serif;
    font-size: 14px;
    color: var(--ink-white);
    padding-top: 2px;
  }
  .net-weight {
    position: absolute;
    top: 556px;
    left: 0;
    right: 0;
    display: flex;
    justify-content: center;
    align-items: center;
    gap: 8px;
    font-family: "Cinzel", serif;
    font-size: 10px;
    letter-spacing: 0.5px;
    color: var(--ink-soft);
  }
</style>
</head>
<body>
<main class="canvas">
  <section class="bag-front">
    <p class="category">GREEN COFFEE</p>
    <h1 class="brand-name">BREW<br>HAUNT</h1>
    <div class="brand-mark"><span class="dot"></span>BrewHaunt</div>
    <div class="web-ribbon">
      <svg width="200" height="36" viewBox="0 0 200 36" aria-hidden="true">
        <polygon points="0,10 26,10 26,32 0,32 8,21" fill="var(--ribbon-green)"/>
        <polygon points="200,10 174,10 174,32 200,32 192,21" fill="var(--ribbon-green)"/>
        <polygon points="20,32 26,32 26,36" fill="var(--ribbon-shade)"/>
        <polygon points="180,32 174,32 174,36" fill="var(--ribbon-shade)"/>
        <rect x="20" y="4" width="160" height="28" fill="var(--ribbon-green)"/>
      </svg>
      <span class="web-address">brewhaunt.com.au</span>
    </div>
    <p class="net-weight">NET WT. 12 OZ.</p>
  </section>
</main>
</body>
</html>
```